Medical Device Packaging Project 3 of 5

We are a medical device startup company needing packaging for a total of 5 device brands. This is posting 3 of 5 and the device name is "Venor"

Venor is an intraocular lens for use in cataract surgery. The target market is Chinese ophthalmologists. The box should be sophisticated and upmarket.

The company name is Tamsin Medica, I have included the logo in the uploaded files section. You should include the logo on the box.

I have uploaded a sample lens boxes from other companies that demonstrate the information needed to be contained on the box in terms of address, warnings, symbols, etc.

I have also uploaded the blank dieline of the boxes

You are welcome and encouraged to also submit to projects 1, 2, 4, and 5 as well. The same rules and expectations apply.

Requirements
Should not have
• Should not have any images of an eye or any bionic/futuristic feel to the design
• Note that the calvoptix box is for text reference only. You may use the lens image but the futuristic/bionic look is NOT what we are going for with this brand. It should be traditional upmarket medical device artwork.

```html
<!DOCTYPE html>
<html lang="en">
<head>
<meta charset="utf-8">
<title>Venor – Intraocular Lens Packaging</title>
<link href="https://fonts.googleapis.com/css2?family=Oswald:wght@300&family=Roboto+Condensed:wght@400;700&display=swap" rel="stylesheet">
<style>
  :root {
    --page-bg: #f4f6f8;
    --panel-light: #d9f6fb;
    --panel-mid: #8fe3f1;
    --panel-deep: #3fc6de;
    --brand-blue: #1aa9dd;
    --logo-blue: #2a6f9e;
    --navy: #1b2a6b;
    --accent-red: #c8102e;
    --ink: #1d2f3a;
    --white: #ffffff;
  }
  * { margin: 0; padding: 0; box-sizing: border-box; }
  html, body { width: 1200px; height: 800px; overflow: hidden; background: var(--page-bg); }
  body { font-family: "Roboto Condensed", sans-serif; color: var(--ink); }

  .canvas { position: relative; width: 1200px; height: 800px; display: flex; gap: 40px; padding: 120px 40px; }

  .panel {
    position: relative; width: 540px; height: 560px; overflow: hidden;
    background:
      radial-gradient(circle at 50% 45%, rgba(255,255,255,.75) 0, rgba(255,255,255,0) 55%),
      linear-gradient(160deg, var(--panel-light) 0%, var(--panel-mid) 55%, var(--panel-deep) 100%);
    box-shadow: 0 18px 30px rgba(0,0,0,.12);
  }

  .brand-mark { position: absolute; display: flex; align-items: center; gap: 8px; }
  .brand-mark__dot { width: 14px; height: 14px; border-radius: 50%; background: var(--logo-blue); }
  .brand-mark__name { font-weight: 400; font-size: 22px; letter-spacing: 2px; color: var(--logo-blue); text-transform: uppercase; line-height: 1; }

  .product-name {
    position: absolute; font-family: "Oswald", sans-serif; font-weight: 300;
    color: var(--brand-blue); letter-spacing: 2px; line-height: 1;
  }
  .product-name sup { font-family: "Roboto Condensed", sans-serif; font-size: 12px; vertical-align: top; margin-left: 2px; }

  /* Front */
  .front .brand-mark { top: 80px; left: 70px; }
  .front .product-name { top: 90px; left: 0; width: 100%; text-align: center; font-size: 92px; }
  .lens-visual {
    position: absolute; top: 215px; left: 160px; width: 220px; height: 220px; border-radius: 50%;
    background: radial-gradient(circle at 40% 35%, #f4f4f4 0%, #b9bcc0 45%, #5e6367 100%);
  }
  .front .lens-type { position: absolute; top: 455px; width: 100%; text-align: center; font-weight: 700; font-size: 22px; color: var(--navy); }
  .front .optic-profile { position: absolute; top: 485px; width: 100%; text-align: center; font-weight: 700; font-size: 36px; color: var(--accent-red); }
  .front .edge-design { position: absolute; top: 528px; width: 100%; text-align: center; font-size: 22px; color: var(--ink); }

  /* Back */
  .language-list { position: absolute; top: 78px; left: 18px; list-style: none; }
  .language-list li { display: flex; gap: 10px; height: 58px; font-size: 11.5px; line-height: 1.35; color: var(--ink); }
  .flag { width: 24px; height: 18px; flex: none; margin-top: 3px; display: flex; }
  .flag span { flex: 1; }
  .flag--col { flex-direction: column; }

  .back .brand-mark { top: 118px; right: 40px; }
  .back .product-name { top: 390px; right: 70px; font-size: 64px; }
  .back .lens-type { position: absolute; top: 462px; right: 70px; font-weight: 700; font-size: 10px; color: var(--navy); }
  .back .edge-design { position: absolute; top: 478px; right: 94px; font-size: 10px; color: var(--ink); }
  .back .edge-design b { font-weight: 700; }

  .symbols { position: absolute; top: 520px; right: 70px; display: flex; align-items: center; gap: 5px; }
  .sterile-badge { display: flex; border: 2px solid var(--white); color: var(--white); font-weight: 700; font-size: 12px; }
  .sterile-badge span { padding: 2px 5px; }
  .sterile-badge span + span { border-left: 2px solid var(--white); }
</style>
</head>
<body>
<main class="canvas">

  <!-- Front face -->
  <section class="panel front">
    <div class="brand-mark"><span class="brand-mark__dot"></span><span class="brand-mark__name">Tamsin Medica</span></div>
    <h1 class="product-name">VENOR<sup>TM</sup></h1>
    <div class="lens-visual" role="img" aria-label="Illustration of a single-piece intraocular lens with curved haptics"></div>
    <p class="lens-type">HYDROPHOBIC ACRYLIC INTRAOCULAR LENS</p>
    <p class="optic-profile">Aspheric</p>
    <p class="edge-design">With 360º square edge</p>
  </section>

  <!-- Back face -->
  <section class="panel back">
    <ul class="language-list">
      <li><span class="flag flag--col"><span style="background:#012169"></span><span style="background:#c8102e"></span><span style="background:#012169"></span></span>
        <p>Contains one sterile intraocular lens<br>Do not use if the packaging is damaged<br>Do not resterilize</p></li>
      <li><span class="flag flag--col"><span style="background:#ae1c28"></span><span style="background:#fff"></span><span style="background:#21468b"></span></span>
        <p>Bevat één steriele intraoculaire lens<br>Niet gebruiken als de verpakking beschadigd is<br>Niet opnieuw steriliseren</p></li>
      <li><span class="flag"><span style="background:#0055a4"></span><span style="background:#fff"></span><span style="background:#ef4135"></span></span>
        <p>Contient une lentille intraoculaire stérile<br>Ne pas utiliser si l'emballage est endommagé<br>Ne pas restériliser</p></li>
      <li><span class="flag flag--col"><span style="background:#000"></span><span style="background:#dd0000"></span><span style="background:#ffce00"></span></span>
        <p>Enthält eine sterile intraokulare Linse<br>Nicht verwenden, wenn die Verpackung beschädigt ist<br>Nicht resterilisieren</p></li>
      <li><span class="flag flag--col"><span style="background:#0d5eaf"></span><span style="background:#fff"></span><span style="background:#0d5eaf"></span><span style="background:#fff"></span><span style="background:#0d5eaf"></span></span>
        <p>Περιέχει ένα αποστειρωμένο ενδοφθάλμιο φακό<br>Μην το χρησιμοποιείτε εάν η συσκευασία έχει υποστεί ζημιά<br>Μην επαναποστειρώνετε</p></li>
      <li><span class="flag"><span style="background:#009246"></span><span style="background:#fff"></span><span style="background:#ce2b37"></span></span>
        <p>Contiene una lente intraoculare sterile<br>Non usare se la confezione è danneggiata<br>Non risterilizzare</p></li>
      <li><span class="flag"><span style="background:#006600;flex:2"></span><span style="background:#ff0000;flex:3"></span></span>
        <p>Contém uma lente intra-ocular esterilizada<br>Não use se a embalagem está danificada<br>Não reesterilize</p></li>
      <li><span class="flag flag--col"><span style="background:#aa151b"></span><span style="background:#f1bf00;flex:2"></span><span style="background:#aa151b"></span></span>
        <p>Contiene una lente intraocular estéril<br>No utilizar si el envase está dañado<br>No vuelva a esterilizar</p></li>
    </ul>

    <div class="brand-mark"><span class="brand-mark__dot"></span><span class="brand-mark__name">Tamsin Medica</span></div>
    <h2 class="product-name">VENOR<sup>TM</sup></h2>
    <p class="lens-type">HYDROPHOBIC ACRYLIC INTRAOCULAR LENS</p>
    <p class="edge-design"><b>Aspheric</b> with 360º square edge</p>

    <div class="symbols">
      <div class="sterile-badge"><span>STERILE</span><span>EO</span></div>
      <svg width="20" height="20" viewBox="0 0 20 20" aria-label="Caution"><path d="M10 2 L18 18 H2 Z" fill="none" stroke="#fff" stroke-width="2"/><path d="M10 8v5M10 15v1" stroke="#fff" stroke-width="2"/></svg>
      <svg width="20" height="20" viewBox="0 0 20 20" aria-label="Do not reuse"><circle cx="10" cy="10" r="8" fill="none" stroke="#fff" stroke-width="2"/><path d="M4 16 16 4" stroke="#fff" stroke-width="2"/></svg>
      <svg width="20" height="20" viewBox="0 0 20 20" aria-label="Do not resterilize"><circle cx="10" cy="10" r="8" fill="none" stroke="#fff" stroke-width="2"/><path d="M4 4 16 16" stroke="#fff" stroke-width="2"/></svg>
      <svg width="20" height="20" viewBox="0 0 20 20" aria-label="Do not use if package is damaged"><circle cx="10" cy="10" r="8" fill="none" stroke="#fff" stroke-width="2"/><rect x="6" y="6" width="8" height="8" fill="#fff"/></svg>
    </div>
  </section>

</main>
</body>
</html>
```